Brelmont Engineering Business Card

our company has just rebranded and taken on a new logo design. We now need to update our business cards with the new logo. This is also an opportunity to reformat and modernize our look. We are an engineering company so the look needs to be formal and professional yet it should look modern. Have a look at our current card and the new card should have the same information.

Target Market(s)

Engineering firms, government, mining companies

Industry/Entity Type

Mechanical Engineering

Contact Information for Business Card

Requirements
Must have
• look professional and modern
Should not have
• should not include the office locations 'Brisbane, Sydney and Kuala Lumpur'
• you will find this on the example but it should not be included in these versions. please remove from your submissions and resubmit

```html
<!DOCTYPE html>
<html lang="en">
<head>
<meta charset="utf-8">
<title>Brelmont Engineering — Business Card</title>
<link rel="stylesheet" href="https://fonts.googleapis.com/css2?family=Open+Sans:wght@400;600;700&family=Exo+2:wght@500&display=swap">
<style>
  :root {
    --backdrop: #d8d5d1;
    --card: #ecedee;
    --brand-blue: #3b4aa4;
    --ink: #2b2b33;
    --white: #ffffff;
  }
  * { margin: 0; padding: 0; box-sizing: border-box; }
  html, body {
    width: 1200px;
    height: 941px;
    overflow: hidden;
    background: var(--backdrop);
  }
  .stage {
    width: 1200px;
    height: 941px;
    display: flex;
    align-items: center;
    justify-content: center;
  }
  .card {
    position: relative;
    width: 480px;
    height: 800px;
    background: var(--card);
    border-radius: 34px;
    overflow: hidden;
    box-shadow: 0 6px 18px rgba(0,0,0,0.18);
    font-family: "Open Sans", sans-serif;
  }
  .brand {
    position: absolute;
    left: 58px;
    top: 150px;
    display: flex;
    align-items: center;
    gap: 18px;
  }
  .brand-dot {
    width: 62px;
    height: 62px;
    border-radius: 50%;
    background: var(--brand-blue);
    flex: none;
  }
  .brand-name {
    font-family: "Open Sans", sans-serif;
    font-weight: 700;
    font-size: 31px;
    line-height: 1.05;
    color: var(--brand-blue);
    letter-spacing: 0.5px;
  }
  .rule {
    position: absolute;
    left: 0;
    width: 100%;
    height: 5px;
    background: var(--brand-blue);
  }
  .rule--top { top: 316px; }
  .rule--bottom { top: 468px; }
  .band {
    position: absolute;
    left: 0;
    top: 332px;
    width: 100%;
    height: 124px;
    background: var(--brand-blue);
    padding: 28px 0 0 58px;
  }
  .person-name {
    font-size: 30px;
    font-weight: 400;
    letter-spacing: 0.5px;
    color: var(--white);
    line-height: 1.2;
  }
  .person-name .given { color: var(--ink); }
  .person-role {
    font-size: 21px;
    color: var(--white);
    margin-top: 4px;
  }
  .contact {
    position: absolute;
    left: 58px;
    top: 560px;
    list-style: none;
    font-family: "Exo 2", sans-serif;
    font-weight: 500;
    font-size: 17px;
    line-height: 1.75;
    color: var(--ink);
  }
  .contact .address { font-family: "Open Sans", sans-serif; font-size: 18px; }
</style>
</head>
<body>
<main class="stage">
  <article class="card">
    <header class="brand">
      <span class="brand-dot"></span>
      <span class="brand-name">Brelmont<br>Engineering</span>
    </header>

    <div class="rule rule--top"></div>
    <section class="band">
      <p class="person-name"><span class="given">DANIEL</span> HARTWELL</p>
      <p class="person-role">Managing Director</p>
    </section>
    <div class="rule rule--bottom"></div>

    <ul class="contact">
      <li class="address">041.12th floor,Harbour Crest Road NTH</li>
      <li class="phone">015 482 3907</li>
      <li class="email">info@brelmont.com</li>
      <li class="web">brelmont.com</li>
    </ul>
  </article>
</main>
</body>
</html>
```